Varnok Develoipment and Management Corp Web Design Project

Website... Based on logo. Update forthcoming....
Updates

Reason: Extended to include recently completed logo design.

Target Market(s)

Financiers, investors, public officials, and landowners.

Industry/Entity Type

Management

Requirements
Should not have
• No palm trees, mayan ruins, or other Caribbean references.

```html
<!DOCTYPE html>
<html lang="en">
<head>
<meta charset="utf-8">
<title>Varnok Develoipment and Management Corp</title>
<link rel="stylesheet" href="https://fonts.googleapis.com/css2?family=Questrial&family=Arimo:ital,wght@0,400;1,400&family=Source+Sans+3:wght@400&display=swap">
<style>
:root{
  --orange:#f7931e;
  --orange-dark:#e8780f;
  --black:#0b0b0b;
  --ink:#222;
  --body:#4a4a4a;
  --link:#1a8fd6;
  --grey-band:#a9abad;
  --photo-tone:#e3e8f1;
  --avatar-tone:#b98a6e;
  --white:#fff;
}
*{margin:0;padding:0;box-sizing:border-box}
html,body{width:1034px;height:1200px;overflow:hidden;background:var(--white)}
.page{position:relative;width:1034px;height:1200px;font-family:"Arimo",Arial,sans-serif;color:var(--ink)}
.abs{position:absolute}

/* header */
.site-header{left:0;top:0;width:1034px;height:92px;background:var(--black)}
.header-rule{left:0;top:92px;width:1034px;height:6px;background:var(--orange)}
.brand{left:126px;top:32px;font-family:"Questrial",sans-serif;font-size:27px;letter-spacing:1px;color:var(--orange);line-height:1}
.main-nav{top:29px;left:399px;height:36px;display:flex;align-items:center;font-family:"Source Sans 3",sans-serif;font-size:14px;color:var(--orange)}
.main-nav a{color:inherit;text-decoration:none;margin-right:26px;line-height:36px}
.main-nav a:last-child{margin-right:0}
.main-nav a.active{background:var(--orange);color:var(--white);border-radius:3px;padding:0 13px;margin-right:14px}

/* hero */
.hero{left:0;top:98px;width:1034px;height:432px;background:
  radial-gradient(ellipse at 20% 30%,#cfeef6 0%,transparent 55%),
  linear-gradient(100deg,#bfe5f0 0%,#e4f5fa 35%,#d3eef6 60%,#eef9fc 100%)}
.hero-photo{left:620px;top:98px;width:320px;height:432px;background:linear-gradient(180deg,#e8eef5 0%,var(--photo-tone) 100%)}
.hero-base{left:0;top:530px;width:1034px;height:6px;background:var(--grey-band)}
.hero-card{left:149px;top:255px;width:391px;height:163px;background:rgba(28,29,30,.95);padding:26px 20px 0 20px;font-family:"Questrial",sans-serif}
.hero-card h2{font-weight:400;font-size:23px;color:var(--orange);line-height:1;margin-bottom:12px}
.hero-card p{font-size:14px;color:#f2f2f2;line-height:17px;margin-bottom:14px}
.btn-learn{display:inline-block;background:var(--orange);color:var(--white);font-size:15px;padding:0 14px;line-height:33px;border-radius:2px;margin-left:-4px}
.slider-arrow{top:308px;width:30px;height:35px;background:#3a3b3c}
.slider-arrow.prev{left:49px}
.slider-arrow.next{left:980px}

/* sections */
.section-title{left:0;width:1034px;text-align:center;font-size:20px;font-weight:400;color:var(--ink);letter-spacing:.3px}
.welcome-text{left:200px;top:585px;width:634px;text-align:center;font-size:12.5px;line-height:19px;color:var(--body)}
.btn-read{left:466px;top:637px;width:102px;height:32px;border-radius:4px;background:linear-gradient(180deg,#f6a035,var(--orange-dark));color:var(--white);font-size:13px;text-align:center;line-height:32px}

.service-label{top:739px;width:200px;text-align:center;font-size:11.5px;color:var(--ink);letter-spacing:.2px}
.service-tile{top:762px;width:155px;height:123px;border-radius:4px;box-shadow:0 7px 8px -4px rgba(0,0,0,.35);overflow:hidden}
.service-tile svg{display:block}
.tile-orange{background:linear-gradient(135deg,#f39a1e 50%,#e8800f 50%)}
.tile-black{background:linear-gradient(135deg,#0a0a0a 50%,#141414 50%)}
.tile-charcoal{background:linear-gradient(135deg,#232323 50%,#2c2c2c 50%)}
.tile-grey{background:linear-gradient(135deg,#4b4b4b 50%,#555 50%)}

.avatar{left:243px;top:957px;width:106px;height:106px;border-radius:50%;background:var(--avatar-tone)}
.quote-date{left:640px;top:953px;width:149px;text-align:right;font-size:11px;color:var(--link);text-decoration:underline}
.quote-mark{font-family:Georgia,serif;font-size:60px;color:#f6d3ce;line-height:1}
.quote-text{left:362px;top:970px;width:440px;font-size:11px;line-height:19px;color:var(--body)}
.quote-author{left:362px;top:1034px;font-size:13px;font-style:italic;color:var(--link)}

/* footer */
.site-footer{left:0;top:1075px;width:1034px;height:125px;background:var(--black)}
.footer-nav{left:0;top:1095px;width:1034px;display:flex;justify-content:center;font-family:"Source Sans 3",sans-serif;font-size:14px;color:#eee}
.footer-nav span{margin:0 13px}
.social-row{left:0;top:1132px;width:1034px;display:flex;justify-content:center;gap:6px}
.social-row span{width:26px;height:26px;border-radius:50%;background:#e6e6e6}
.copyright{left:0;top:1175px;width:1034px;text-align:center;font-family:"Source Sans 3",sans-serif;font-size:10px;color:#bbb}
</style>
</head>
<body>
<div class="page">
  <header class="abs site-header"></header>
  <div class="abs header-rule"></div>
  <div class="abs brand">VARNOK</div>
  <nav class="abs main-nav">
    <a class="active">HOME</a><a>ABOUT US</a><a>SERVICES</a><a>NEWS</a><a>TESTIMONIALS</a><a>CONTACT US</a>
  </nav>

  <div class="abs hero" role="img" aria-label="Softly blurred bright office interior"></div>
  <div class="abs hero-photo" role="img" aria-label="Photo of a smiling professional woman"></div>
  <div class="abs hero-base"></div>
  <div class="abs hero-card">
    <h2>A Little About Me...</h2>
    <p>Lorem ipsum dolor sit amet, consectetur adipiscing elit,<br>sed do eiusmod tempor incididunt.</p>
    <span class="btn-learn">LEARN MORE</span>
  </div>
  <div class="abs slider-arrow prev"><svg width="30" height="35" viewBox="0 0 30 35"><path d="M18 9 L11 17.5 L18 26" fill="none" stroke="#ddd" stroke-width="1.2"/></svg></div>
  <div class="abs slider-arrow next"><svg width="30" height="35" viewBox="0 0 30 35"><path d="M12 9 L19 17.5 L12 26" fill="none" stroke="#ddd" stroke-width="1.2"/></svg></div>

  <h1 class="abs section-title" style="top:553px">WELCOME</h1>
  <p class="abs welcome-text">Sed ut perspiciatis unde omnis iste natus error sit voluptatem accusantium doloremque laudantium, totam rem aperiam, eaque ipsa quae ab illo inventore</p>
  <div class="abs btn-read">Read More</div>

  <h2 class="abs section-title" style="top:700px">SERVICES WE PROVIDE ARE</h2>
  <div class="abs service-label" style="left:142px">INVESTMENT DEVELOPMENT</div>
  <div class="abs service-label" style="left:322px">MANAGEMENT</div>
  <div class="abs service-label" style="left:507px">PROJECT STAKEHOLDERS</div>
  <div class="abs service-label" style="left:687px">LANDOWNERS</div>

  <div class="abs service-tile tile-orange" style="left:164px">
    <svg width="155" height="123" viewBox="0 0 155 123" fill="none" stroke="#3a2a10" stroke-width="1.3">
      <path d="M42 48 L77 25 L112 48 Z"/><rect x="45" y="48" width="64" height="6"/>
      <rect x="51" y="56" width="8" height="30"/><rect x="65" y="56" width="8" height="30"/><rect x="81" y="56" width="8" height="30"/><rect x="95" y="56" width="8" height="30"/>
      <rect x="46" y="86" width="62" height="5"/><rect x="41" y="91" width="72" height="6"/>
    </svg>
  </div>
  <div class="abs service-tile tile-black" style="left:348px">
    <svg width="155" height="123" viewBox="0 0 155 123" fill="none" stroke="#d8d8d8" stroke-width="1.3">
      <rect x="41" y="38" width="65" height="45" rx="5"/><path d="M63 38 V29 H84 V38"/><path d="M41 58 H106"/><rect x="68" y="55" width="11" height="7"/>
    </svg>
  </div>
  <div class="abs service-tile tile-charcoal" style="left:532px">
    <svg width="155" height="123" viewBox="0 0 155 123" fill="none" stroke="#d8d8d8" stroke-width="1.3">
      <circle cx="56" cy="37" r="9"/><circle cx="98" cy="37" r="9"/><path d="M42 70 C42 52 70 50 70 62"/><path d="M112 70 C112 52 84 50 84 62"/>
      <circle cx="77" cy="51" r="13"/><path d="M52 92 C52 68 102 68 102 92 Z"/>
    </svg>
  </div>
  <div class="abs service-tile tile-grey" style="left:715px">
    <svg width="155" height="123" viewBox="0 0 155 123" fill="none" stroke="#e2e2e2" stroke-width="1.3">
      <circle cx="79" cy="44" r="13"/><path d="M54 86 C54 58 104 58 104 86 Z" stroke-linejoin="round"/>
    </svg>
  </div>

  <h2 class="abs section-title" style="top:911px">TESTIMONIALS</h2>
  <div class="abs avatar" role="img" aria-label="Photo of the client giving the testimonial"></div>
  <div class="abs quote-date">Date : 24-04-2014</div>
  <div class="abs quote-mark" style="left:356px;top:960px">&ldquo;</div>
  <div class="abs quote-mark" style="left:553px;top:1000px">&rdquo;</div>
  <p class="abs quote-text">Sed ut perspiciatis unde omnis iste natus error sit voluptatem accusantium doloremque laudantium, totam rem aperiam, eaque ipsa quae ab illo inventore veritatis et quasi architecto beatae vitae dicta sunt explicabo.</p>
  <div class="abs quote-author">- Author Name</div>

  <footer class="abs site-footer"></footer>
  <nav class="abs footer-nav"><span>Home</span><span>About Us</span><span>Services</span><span>News</span><span>Testimonials</span><span>Contact Us</span></nav>
  <div class="abs social-row"><span></span><span></span><span></span><span></span><span></span></div>
  <div class="abs copyright">&copy; 2014. www.varnokdm.com</div>
</div>
</body>
</html>
```